Web Design for Financial Consulting Company

We need a website design for a financial consulting company "Kelvane Consulting". We build financial models, scenario analysis, handle the budgeting process and provide temporary staffing. I have over 10 years of experience. My Excel expertise and analytical savvy has saved clients over $17 million in profit.

Target Market(s)

Small to medium businesses

Industry/Entity Type

Financial Consulting

Number of Pages Required

4 page

Requirements
Must have
• Professional looking
Nice to have
• A little futuristic looking

```html
<!DOCTYPE html>
<html lang="en">
<head>
<meta charset="utf-8">
<title>Kelvane Consulting</title>
<link rel="stylesheet" href="https://fonts.googleapis.com/css2?family=Montserrat:wght@400;500;600;700&display=swap">
<style>
:root{
  --ink:#0a0a0c;
  --white:#ffffff;
  --blue:#13a6ec;
  --blue-light:#8fd6f6;
  --slate:#3a5265;
  --line:#3a3a40;
  --text:#222428;
  --muted:#6b6e74;
  --field:#d9dbde;
}
*{box-sizing:border-box;margin:0;padding:0}
html,body{width:1200px;height:4278px;overflow:hidden}
body{position:relative;background:var(--white);font-family:'Montserrat',sans-serif;color:var(--text)}
.abs{position:absolute}
a{color:inherit;text-decoration:none}

/* brand */
.brand{position:absolute;display:flex;align-items:center;gap:10px;font-weight:600;font-size:19px;letter-spacing:1.5px;text-transform:uppercase;color:var(--white)}
.brand-square{width:22px;height:22px;background:var(--blue)}
.nav{position:absolute;display:flex;align-items:center;font-size:13px;color:var(--white)}
.nav a{margin-right:34px}
.btn-talk{background:var(--white);color:var(--blue);padding:8px 16px;font-size:13px;border-radius:2px}

/* hero */
.hero{position:absolute;left:0;top:0;width:1200px;height:526px;background:linear-gradient(100deg,#1c1c1f 0%,#2c2d31 38%,#4a4e55 62%,#3a3d42 100%)}
.hero-title{position:absolute;left:196px;top:203px;color:var(--white);font-size:31px;font-weight:600;letter-spacing:2.5px;line-height:42px}
.hero-sub{position:absolute;left:233px;top:305px;color:var(--white);font-size:13px}
.hero-sub span{color:var(--blue)}
.hero-cta{position:absolute;left:366px;top:344px;display:flex;align-items:center;gap:14px;color:var(--white);font-size:12px;letter-spacing:.5px}
.circle-arrow{width:31px;height:31px;border:1.5px solid var(--white);border-radius:50%;display:flex;align-items:center;justify-content:center}
.hero-tab{position:absolute;top:467px;width:141px;padding-bottom:10px;border-bottom:1px solid #9a9ca0;color:var(--white);font-size:12.5px}

/* about */
.about-photo{position:absolute;left:141px;top:634px;width:490px;height:325px;background:linear-gradient(135deg,#c9ccd1 0%,#7f858c 45%,#2e3136 100%)}
.eyebrow{font-size:12px;font-weight:500}
.about-text{position:absolute;left:709px;top:634px;width:350px}
.about-text h2{font-size:22px;font-weight:500;letter-spacing:.5px;margin:12px 0 30px}
.about-text p{font-size:11.5px;line-height:21.4px}
.btn-outline{display:inline-block;border:1px solid var(--blue);color:var(--text);font-size:12px;padding:8px 16px;border-radius:2px}
.vline{position:absolute;width:2px;background:var(--blue)}

/* services */
.services{position:absolute;left:0;top:1077px;width:1200px;height:958px;background:var(--ink);color:var(--white)}
.services .eyebrow{position:absolute;left:141px;top:128px;color:var(--white)}
.services h2{position:absolute;left:141px;top:156px;width:500px;font-size:24.5px;font-weight:500;line-height:33px}
.acc-row{position:absolute;left:141px;width:925px;border-bottom:1px solid var(--line);display:flex;justify-content:space-between;align-items:center;padding-bottom:14px;font-size:13px;font-weight:600;letter-spacing:.5px}
.acc-icon{font-weight:300;font-size:20px;line-height:1}
.acc-list{position:absolute;left:141px;top:484px;font-size:12px;list-style:none;color:#d8d9dc}
.acc-list li{margin-bottom:15px}
.acc-list li::before{content:"→";color:var(--blue);margin-right:8px}
.acc-photo{position:absolute;left:671px;top:483px;width:395px;height:195px;background:linear-gradient(120deg,#53565b,#8b8e93 55%,#cfd1d3 70%,#45484d)}

/* clients */
.clients-head{position:absolute;left:0;width:1200px;text-align:center}
.clients-head h2,.industries h2{font-size:23px;font-weight:500;letter-spacing:1px;margin-top:12px}
.client{position:absolute;width:170px;margin-left:-85px;text-align:center;font-size:19px;font-weight:700;color:var(--ink);display:flex;align-items:center;justify-content:center;gap:8px}
.client i{width:12px;height:12px;background:var(--ink);display:inline-block}

/* get in touch */
.touch{position:absolute;left:0;top:2392px;width:1200px;height:606px;clip-path:polygon(0 0,100% 0,100% 538px,0 606px);background:linear-gradient(160deg,#2a2b2f 0%,#1a1b1e 45%,#0c0d10 100%);color:var(--white)}
.touch-photo{position:absolute;left:0;top:0;width:700px;height:606px;background:radial-gradient(ellipse at 35% 40%,#55585e 0%,#2f3135 45%,rgba(12,13,16,0) 80%)}
.touch-title{position:absolute;left:141px;top:112px;font-size:24px;font-weight:500;letter-spacing:1px}
.touch-copy{position:absolute;left:647px;top:110px;width:380px;font-size:19px;font-weight:500;line-height:26px}
.touch-btn{position:absolute;left:647px;top:216px;background:var(--white);color:var(--text);font-size:12px;padding:7px 16px;border-radius:2px}
.stay{position:absolute;left:647px;top:377px;font-size:19px;font-weight:500}
.newsletter{position:absolute;left:647px;top:418px;width:412px;height:36px;border:1px solid #c8c9cc;border-radius:3px;display:flex;justify-content:space-between;align-items:center;font-size:12px;padding-left:16px;color:#e5e6e8}
.newsletter span{background:var(--blue);color:var(--white);height:34px;width:96px;display:flex;align-items:center;justify-content:center;border-radius:0 3px 3px 0}

/* industries */
.industries{position:absolute;right:141px;top:3008px;text-align:right}
.card{position:absolute;top:3096px;height:206px;background:var(--slate);color:var(--white)}
.card .label{position:absolute;left:17px;bottom:14px;font-size:13.5px;font-weight:600;line-height:21px}
.card svg{position:absolute;right:15px;top:15px}
.card-photo{background:linear-gradient(140deg,#2e4a5a 0%,#5d7b86 40%,#c9d3d2 65%,#3d5864 100%)}

/* contact */
.dark-base{position:absolute;left:0;top:3723px;width:1200px;height:555px;background:var(--ink);clip-path:polygon(0 70px,100% 0,100% 100%,0 100%)}
.contact-card{position:absolute;left:128px;top:3453px;width:943px;height:519px;background:var(--white);border:1px solid #e4e5e7}
.contact-card h2{position:absolute;left:0;top:41px;width:100%;text-align:center;font-size:23px;font-weight:500}
.contact-card p{position:absolute;left:0;top:88px;width:100%;text-align:center;font-size:12px;line-height:19px;color:var(--muted)}
.field{position:absolute;border:1px solid var(--field);font-size:12px;color:var(--muted);padding:0 16px;display:flex;align-items:center}
.field.area{align-items:flex-start;padding-top:17px}
.send{position:absolute;left:420px;top:430px;width:101px;height:38px;border:1px solid var(--blue);font-size:12px;display:flex;align-items:center;justify-content:center;border-radius:2px}

/* footer */
.footer{color:var(--white);font-size:12.5px}
.social{position:absolute;top:4146px;left:132px;display:flex;gap:12px;font-size:10px;color:var(--white)}
.contact-line{position:absolute;left:627px;font-size:13px;color:var(--white)}
.contact-line b{font-weight:400;color:#9a9ca0;display:inline-block;width:25px}
.address{position:absolute;left:875px;top:4124px;width:190px;font-size:12px;line-height:16px;color:#cfd0d3}
.copyright{position:absolute;left:128px;top:4228px;font-size:11.5px;color:#8c8e92}
</style>
</head>
<body>

<header>
  <div class="hero" role="img" aria-label="Hands on a laptop keyboard with rising financial bar charts overlaid"></div>
  <div class="brand" style="left:131px;top:29px"><span class="brand-square"></span>Kelvane Consulting</div>
  <nav class="nav" style="left:620px;top:25px">
    <a>Home</a><a>About Us</a><a>Services</a><a>Contact Us</a>
    <a class="btn-talk">Lats Talk</a>
  </nav>
  <h1 class="hero-title">EMPOWERING YOUR<br>FINANCIAL SUCCESS</h1>
  <p class="hero-sub">Helping your <span>finance team</span> and <span>increasing profit</span></p>
  <a class="hero-cta">CONTACT WITH US <span class="circle-arrow"><svg width="14" height="10" viewBox="0 0 14 10"><path d="M0 5h12M8 1l4 4-4 4" stroke="#13a6ec" stroke-width="1.4" fill="none"/></svg></span></a>
  <div class="hero-tab" style="left:141px">Expert Insights</div>
  <div class="hero-tab" style="left:395px">Strategic Solutions</div>
  <div class="hero-tab" style="left:649px">Reliable Results</div>
  <div class="hero-tab" style="left:905px">Proven Success</div>
</header>

<section class="about">
  <div class="about-photo" role="img" aria-label="Desk with laptop, plant and financial data table overlay"></div>
  <div class="about-text">
    <div class="eyebrow">About Us</div>
    <h2>KELVANE CONSULTING</h2>
    <p>At Kelvane Consulting, We Are A Team Of Experienced Finance Professionals Dedicated To Helping Businesses Thrive. With Over 10 Years Of Expertise In The Industry, We Specialize In Developing Strategic Financial Plans, Providing Insightful Analysis, And Supporting Decision-Making Processes. Our Track Record Speaks For Itself, Having Successfully Increased Profitability For Our Clients By A Remarkable $17 Million.</p>
    <a class="btn-outline" style="margin-top:28px">Find Out More</a>
  </div>
</section>
<div class="vline" style="left:598px;top:790px;height:334px"></div>

<section class="services">
  <div class="eyebrow">What We Do</div>
  <h2>We provide comprehensive financial consulting services to help businesses optimize their financial strategies and achieve sustainable growth.</h2>
  <svg class="abs" style="left:1014px;top:125px" width="51" height="51" viewBox="0 0 51 51"><rect x="0" y="0" width="25" height="25" fill="#8fd6f6"/><rect x="25" y="0" width="26" height="51" fill="#13a6ec"/><rect x="13" y="25" width="12" height="12" fill="#13a6ec"/></svg>
  <div class="acc-row" style="top:349px">Financial Models – Projects<span class="acc-icon">+</span></div>
  <div class="acc-row" style="top:415px">Budgeting Process<span class="acc-icon">×</span></div>
  <ul class="acc-list">
    <li>Building budgets from scratch</li>
    <li>Revamping current process to be more robust and scalable.</li>
  </ul>
  <div class="acc-photo" role="img" aria-label="Budget planning note on a desk with notebook and pens"></div>
  <div class="acc-row" style="top:718px">Temporary Staffing<span class="acc-icon">+</span></div>
  <div class="acc-row" style="top:785px">Data Cleansing<span class="acc-icon">+</span></div>
  <div class="acc-row" style="top:851px">Process Improvement<span class="acc-icon">+</span></div>
</section>

<section>
  <div class="clients-head" style="top:2095px">
    <div class="eyebrow">Clients</div>
    <h2>TRUST US</h2>
  </div>
  <div class="client" style="left:299px;top:2200px"><i></i>Lumenfold</div>
  <div class="client" style="left:526px;top:2200px">Orchard Works</div>
  <div class="client" style="left:739px;top:2200px">Tessary</div>
  <div class="client" style="left:933px;top:2200px">Bank Halvern</div>
  <div class="client" style="left:299px;top:2281px">Corvina</div>
  <div class="client" style="left:526px;top:2281px">Brightmoor</div>
  <div class="client" style="left:739px;top:2281px">Ridgeline</div>
  <div class="client" style="left:933px;top:2281px">Bayfield Pipe</div>
</section>

<section class="touch">
  <div class="touch-photo" role="img" aria-label="Open hands holding a glowing gear with a group icon"></div>
  <h2 class="touch-title">GET IN TUCH</h2>
  <p class="touch-copy">Unlock your financial potential with our strategic consulting. Get in touch now to get started.</p>
  <a class="touch-btn">Lats Talk</a>
  <h3 class="stay">Stay Informed</h3>
  <div class="newsletter">Your Email<span>Subscribe</span></div>
</section>
<div class="vline" style="left:598px;top:2352px;height:329px"></div>

<section>
  <div class="industries">
    <div class="eyebrow">Industries</div>
    <h2>WE SERVE</h2>
  </div>
  <div class="card" style="left:138px;width:207px"><svg width="24" height="24" viewBox="0 0 24 24"><path d="M2 22L22 2M8 2h14v14" stroke="#fff" stroke-width="1.6" fill="none"/></svg><div class="label">Banking And<br>Finance</div></div>
  <div class="card card-photo" style="left:365px;width:223px;height:222px" role="img" aria-label="Laptop with code overlay on a desk"><svg width="24" height="24" viewBox="0 0 24 24"><path d="M2 22L22 2M8 2h14v14" stroke="#13a6ec" stroke-width="1.6" fill="none"/></svg></div>
  <div class="abs" style="left:382px;top:3327px;font-size:13.5px;font-weight:600;line-height:21px">Technology And<br>Software</div>
  <div class="card" style="left:608px;width:207px"><svg width="24" height="24" viewBox="0 0 24 24"><path d="M2 22L22 2M8 2h14v14" stroke="#fff" stroke-width="1.6" fill="none"/></svg><div class="label">Manufacturing And<br>Engineering</div></div>
  <div class="card" style="left:835px;width:206px"><svg width="24" height="24" viewBox="0 0 24 24"><path d="M2 22L22 2M8 2h14v14" stroke="#fff" stroke-width="1.6" fill="none"/></svg><div class="label">Healthcare And<br>Pharmaceuticals</div></div>
  <div class="card" style="left:1061px;width:139px"><div class="label">Retail And E-<br>Commerce</div></div>
</section>

<div class="dark-base"></div>
<svg class="abs" style="left:113px;top:3438px" width="51" height="48" viewBox="0 0 51 48"><rect x="0" y="0" width="51" height="24" fill="#13a6ec"/><rect x="0" y="24" width="15" height="24" fill="#8fd6f6"/></svg>
<section class="contact-card">
  <h2>CONTACT US</h2>
  <p>Contact us today and let's explore the possibilities of unlocking your<br>business full potential.</p>
  <div class="field" style="left:60px;top:159px;width:398px;height:39px">Your name</div>
  <div class="field" style="left:495px;top:159px;width:390px;height:39px">Last name</div>
  <div class="field" style="left:60px;top:217px;width:398px;height:37px">Your phone</div>
  <div class="field" style="left:495px;top:217px;width:395px;height:37px">Your email</div>
  <div class="field area" style="left:60px;top:284px;width:830px;height:116px">Type your message here...</div>
  <div class="send">Send Us</div>
</section>

<footer class="footer">
  <div class="brand" style="left:131px;top:4063px"><span class="brand-square"></span>Kelvane Consulting</div>
  <nav class="nav" style="left:626px;top:4066px;font-size:12.5px">
    <a style="margin-right:29px">Home</a><a style="margin-right:29px">About Us</a><a style="margin-right:29px">Services</a><a style="margin-right:29px">Contact Us</a>
    <a class="btn-talk" style="color:var(--text)">Lats Talk</a>
  </nav>
  <div class="social"><span>Orbit</span><span>Relay</span><span>Pixa</span></div>
  <div class="contact-line" style="top:4125px"><b>T:</b>(555) 014-2287</div>
  <div class="contact-line" style="top:4155px"><b>E:</b>hello@kelvane.example</div>
  <div class="address">2210 Alder Lane, Fairhaven, Oregon 97031</div>
  <div class="copyright">Copyright Kelvane Consulting LLC | All rights reserved</div>
</footer>

</body>
</html>
```